Business Card Design for ReaL ESTATE AGENT

New Business Cards for a real estate agent in Jacksonville, FL. My specialty is urban core, historic districts but sell through out the city. Company Name is Quill and Harbor Realty a division of the Vantrell Companies. The card needs to convey an essence of professionalism, knowledge and success.

Target Market(s)

Home buyers and Sellers

Industry/Entity Type

Real Estate

Contact Information for Business Card

Double sided

Font styles to use
Sans Serif

Requirements
Must have
• My logs and photo (provided). My contact information as follows:
• Derek Holloway
• Cell 904-618-3092
• Office 904-731-6248
• Email derekholloway@mailvantor.com
Nice to have
• Tag Line - Exceptional Effort. Proven Results.

```html
<!DOCTYPE html>
<html lang="en">
<head>
<meta charset="utf-8">
<title>Quill and Harbor Realty – Business Card</title>
<link href="https://fonts.googleapis.com/css2?family=Open+Sans:wght@400;600;700&display=swap" rel="stylesheet">
<style>
  :root {
    --backdrop: #161616;
    --card: #ffffff;
    --brand-green: #22664a;
    --text-dark: #333333;
    --photo-top: #6f6a66;
    --photo-bottom: #2b2d33;
  }
  * { margin: 0; padding: 0; box-sizing: border-box; }
  html, body {
    width: 1200px;
    height: 900px;
    overflow: hidden;
    background: var(--backdrop);
    font-family: "Open Sans", sans-serif;
  }
  .stage { position: relative; width: 1200px; height: 900px; }
  .card {
    position: absolute;
    top: 170px;
    width: 347px;
    height: 561px;
    background: var(--card);
  }
  .card--front { left: 259px; }
  .card--back { left: 631px; }
  .tab {
    position: absolute;
    left: 102px;
    width: 143px;
    background: var(--brand-green);
  }
  .tab--top { top: 0; height: 30px; }
  .tab--bottom { bottom: 0; height: 28px; }
  .portrait {
    position: absolute;
    left: 102px;
    top: 102px;
    width: 145px;
    height: 173px;
    background: linear-gradient(180deg, var(--photo-top), var(--photo-bottom));
  }
  .identity {
    position: absolute;
    top: 343px;
    left: 0;
    width: 100%;
    text-align: center;
  }
  .identity__name {
    font-weight: 700;
    font-size: 18px;
    color: var(--brand-green);
    letter-spacing: 0.2px;
  }
  .identity__title {
    font-size: 14px;
    color: var(--text-dark);
    margin-top: 1px;
  }
  .contact {
    position: absolute;
    top: 410px;
    left: 0;
    width: 100%;
    text-align: center;
    font-size: 14px;
    color: var(--text-dark);
    line-height: 20px;
  }
  .contact__line { display: flex; justify-content: center; align-items: center; gap: 7px; }
  .contact__icon { width: 11px; height: 11px; flex: none; }
  .brand {
    position: absolute;
    top: 0;
    left: 0;
    width: 100%;
    height: 100%;
    display: flex;
    flex-direction: column;
    align-items: center;
    justify-content: center;
    gap: 14px;
  }
  .brand__mark {
    width: 64px;
    height: 64px;
    background: var(--brand-green);
  }
  .brand__name {
    font-weight: 700;
    font-size: 26px;
    line-height: 1.15;
    color: var(--brand-green);
    text-align: center;
    text-transform: uppercase;
  }
</style>
</head>
<body>
<main class="stage">
  <section class="card card--front">
    <div class="tab tab--top"></div>
    <div class="portrait" role="img" aria-label="Portrait photo of the agent in a dark suit"></div>
    <div class="identity">
      <p class="identity__name">DEREK HOLLOWAY</p>
      <p class="identity__title">Managing Director</p>
    </div>
    <div class="contact">
      <p class="contact__line">
        <svg class="contact__icon" viewBox="0 0 12 12" aria-hidden="true"><path fill="#22664a" d="M1 4c0-2 2-3 5-3s5 1 5 3l-2 1-1-2H4L3 5 1 4zm2 2h6l1 5H2l1-5z"/></svg>
        <span>Cell 904-618-3092</span>
      </p>
      <p class="contact__line">
        <svg class="contact__icon" viewBox="0 0 12 12" aria-hidden="true"><path fill="#22664a" d="M1 4c0-2 2-3 5-3s5 1 5 3l-2 1-1-2H4L3 5 1 4zm2 2h6l1 5H2l1-5z"/></svg>
        <span>Office 904-731-6248</span>
      </p>
      <p class="contact__line">
        <svg class="contact__icon" viewBox="0 0 12 12" aria-hidden="true"><rect x="1" y="3" width="10" height="7" fill="#22664a"/><polyline points="1.5,3.5 6,7 10.5,3.5" fill="none" stroke="#ffffff" stroke-width="1"/></svg>
        <span>derekholloway@mailvantor.com</span>
      </p>
    </div>
    <div class="tab tab--bottom"></div>
  </section>

  <section class="card card--back">
    <div class="tab tab--top"></div>
    <div class="brand">
      <div class="brand__mark"></div>
      <p class="brand__name">Quill and Harbor<br>Realty</p>
    </div>
    <div class="tab tab--bottom"></div>
  </section>
</main>
</body>
</html>
```